Visit card

Industry/Entity Type

Health Care

Contact Information for Business Card

Vobela Care
Odile Ferrandi - chef de Projet

Requirements
Must have
• 318 Hector Delaunay Street 58210 BÉTHUNE Tel: 33 (0) 387 419 264 Mobile: 06 42 93 17 58 Web: www.vobelasystems.example Contact: o.ferrandi@o-vitalesystemes.example
Should not have
• Respect for color

```html
<!DOCTYPE html>
<html lang="fr">
<head>
<meta charset="utf-8">
<title>Vobela Care — Cartes de visite</title>
<link rel="stylesheet" href="https://fonts.googleapis.com/css2?family=Lato:wght@400;700;900&display=swap">
<style>
  :root {
    --backdrop: #1c1c1c;
    --card-dark: #454545;
    --card-light: #ffffff;
    --brand-red: #e0202a;
    --ink: #3a3a3a;
    --ink-soft: #555555;
    --white: #ffffff;
  }
  * { box-sizing: border-box; margin: 0; padding: 0; }
  html, body { width: 1200px; height: 895px; overflow: hidden; }
  body {
    background: var(--backdrop);
    font-family: "Lato", sans-serif;
    position: relative;
  }
  .card {
    position: absolute;
    width: 560px;
    height: 320px;
    box-shadow: 0 10px 30px rgba(0,0,0,.5);
  }

  /* Front */
  .card-front { left: 80px; top: 80px; background: var(--card-dark); }
  .brand-lockup {
    position: absolute; left: 150px; top: 112px;
    display: flex; align-items: center; gap: 20px;
  }
  .brand-dot {
    width: 76px; height: 76px; border-radius: 50%;
    background: var(--white); flex: none;
  }
  .brand-name {
    font-weight: 900; font-size: 34px; letter-spacing: .5px;
    color: var(--white); line-height: 1; white-space: nowrap;
  }
  .front-rule {
    position: absolute; left: 0; right: 0; top: 268px;
    display: flex; align-items: center; gap: 12px;
  }
  .front-rule .line { flex: 1; height: 1.5px; background: var(--brand-red); }
  .front-rule .url {
    font-size: 14px; letter-spacing: 2.5px; color: var(--white); white-space: nowrap;
  }
  .front-rule .url em { font-style: normal; color: var(--brand-red); }

  /* Back */
  .card-back { left: 560px; top: 490px; background: var(--card-light); }
  .back-brand {
    position: absolute; left: 36px; top: 178px;
    display: flex; align-items: center; gap: 12px;
  }
  .back-brand .brand-dot { width: 46px; height: 46px; background: var(--ink); }
  .back-brand .brand-name { font-size: 20px; color: var(--ink); }
  .divider { position: absolute; left: 262px; width: 2px; }
  .divider.top { top: 58px; height: 30px; background: var(--ink-soft); }
  .divider.mid { top: 110px; height: 28px; background: var(--brand-red); }
  .divider.bottom { top: 160px; height: 70px; background: var(--ink-soft); }
  .contact {
    position: absolute; left: 284px; top: 40px;
    color: var(--ink); font-size: 13px; line-height: 1.35;
  }
  .contact .name {
    color: var(--brand-red); font-weight: 900; font-size: 18px;
    text-transform: uppercase; letter-spacing: .3px;
  }
  .contact .role { font-size: 14px; margin-bottom: 12px; }
  .contact .address { margin-bottom: 10px; }
  .contact ul { list-style: none; }
  .contact li { display: flex; align-items: center; gap: 7px; white-space: nowrap; }
  .contact li svg { width: 13px; height: 13px; flex: none; }
</style>
</head>
<body>

<section class="card card-front">
  <div class="brand-lockup">
    <span class="brand-dot"></span>
    <span class="brand-name">Vobela Care</span>
  </div>
  <div class="front-rule">
    <span class="line"></span>
    <span class="url">www.<em>vobelasystems</em>.example</span>
    <span class="line"></span>
  </div>
</section>

<section class="card card-back">
  <div class="back-brand">
    <span class="brand-dot"></span>
    <span class="brand-name">Vobela Care</span>
  </div>
  <span class="divider top"></span>
  <span class="divider mid"></span>
  <span class="divider bottom"></span>
  <div class="contact">
    <p class="name">Odile Ferrandi</p>
    <p class="role">Chef de Projet</p>
    <p class="address">318 Hector Delaunay Street<br>58210 BÉTHUNE</p>
    <ul>
      <li><svg viewBox="0 0 16 16"><circle cx="8" cy="8" r="8" fill="var(--brand-red)"/><rect x="5.5" y="3.5" width="5" height="9" rx="1" fill="none" stroke="#fff" stroke-width="1.3"/></svg>06 42 93 17 58</li>
      <li><svg viewBox="0 0 16 16"><circle cx="8" cy="8" r="8" fill="var(--brand-red)"/><path d="M5 4.5l2 .3.6 2-1.2.9a6 6 0 0 0 2.4 2.4l.9-1.2 2 .6.3 2c-4 .8-7.8-3-7-7z" fill="#fff"/></svg>+33 (0) 387 419 264</li>
      <li><svg viewBox="0 0 16 16"><circle cx="8" cy="8" r="8" fill="var(--brand-red)"/><rect x="4" y="5" width="8" height="6" fill="none" stroke="#fff" stroke-width="1.2"/><path d="M4 5l4 3.5L12 5" fill="none" stroke="#fff" stroke-width="1.2"/></svg>o.ferrandi@o-vitalesystemes.example</li>
      <li><svg viewBox="0 0 16 16"><circle cx="8" cy="8" r="8" fill="var(--brand-red)"/><circle cx="8" cy="8" r="4" fill="none" stroke="#fff" stroke-width="1.1"/><path d="M4 8h8M8 4c-2 2.5-2 5.5 0 8M8 4c2 2.5 2 5.5 0 8" fill="none" stroke="#fff" stroke-width="1"/></svg>www.vobelasystems.example</li>
    </ul>
  </div>
</section>

</body>
</html>
```